Veltrix Stationary

Design the stationary of Veltrix Promotions Group.

Veltrix is a BTL company, BTL meaning "below the line". In other words Veltrix is a Promotional Marketing company (the company that design the brands promotional activities).

The design should transmit creativity, agility, boldness.

I need:
* Bis Card
* Letter head
* Envelopes, both vertical and horizontal (for legal size), and letter envelope
* Folders
* PPT template (Title page and regular page)
* CD slip (CD envelope)
* ID card (employee card)

And what ever else you want to throw in.
Updates

Guys,

Something I missed from the brief.   The predominat color should be RED.

Also, have fun and play with the exclamation mark (!) of the logo. 

Hi guys, more comments:

Remember that Veltrix is a "creativity" agency, not in the advertising side but on the promotional side, and that should reflect on the stationary.

 I want a bold design.  Bold and yet crisp.

 

Guys, i just uploaded the Logo in AI format.

I Also uploaded the actual Veltrix Bis Card, wich I like.  So I will like to see some designs with that bis card approach.

Guys, I am so sorry, but I notice in your last post that I upladed a wrong design ("13154_marketing_group_veltrix_brief225630.ai").  The problem was that I asked the designer the file in AI format and he send me thw wrong file, and since I dont have Illustrator I could not verify it.

The differences are minor, I just already ask him the correct one (similar to the EPS file).

Sorry                                   

Just post the correct AI file : "Veltrix Logo.ai"

Reason: I'm expecting more designs to choose from and also I wont be available tomorrow to decide.

Reason: Sorry guys, but we are not there yet!

Target Market(s)

Marketing directors, Marketing Managers

Industry/Entity Type

Legal

Requirements
Must have
• Must work with the logo attached.
The predominat color should be RED.
Play and have fun with the exclamation mark (!).
Should not have
• * No old fonts

Should not be:
* boring
* Informal
* rigid

```html
<!DOCTYPE html>
<html lang="en">
<head>
<meta charset="utf-8">
<title>Veltrix Promotions Group – Folder Inside</title>
<link href="https://fonts.googleapis.com/css2?family=Arimo:wght@400;700&display=swap" rel="stylesheet">
<style>
  :root {
    --brand-red: #ad0005;
    --paper: #ffffff;
    --ink: #1a1a1a;
    --backdrop: #ffffff;
    --shadow: rgba(0, 0, 0, 0.45);
  }
  * { margin: 0; padding: 0; box-sizing: border-box; }
  html, body {
    width: 1200px;
    height: 900px;
    overflow: hidden;
    background: var(--backdrop);
    font-family: "Arimo", Arial, sans-serif;
    color: var(--ink);
  }
  .canvas {
    position: relative;
    width: 1200px;
    height: 900px;
  }
  .sheet-title {
    position: absolute;
    left: 54px;
    top: 46px;
    font-size: 26px;
    font-weight: 700;
    letter-spacing: 0.2px;
  }
  .folder {
    position: absolute;
    left: 0;
    top: 0;
    width: 1200px;
    height: 900px;
  }
  .folder-art {
    position: absolute;
    inset: 0;
    filter: drop-shadow(5px 5px 4px var(--shadow));
  }
  .brand {
    position: absolute;
    left: 972px;
    top: 130px;
    display: flex;
    flex-direction: column;
    align-items: flex-start;
  }
  .brand-row {
    display: flex;
    align-items: center;
    gap: 6px;
  }
  .brand-name {
    font-size: 30px;
    font-weight: 700;
    line-height: 1;
    color: var(--ink);
    letter-spacing: -0.5px;
  }
  .brand-dot {
    width: 14px;
    height: 14px;
    border-radius: 50%;
    background: var(--brand-red);
  }
  .brand-tagline {
    margin-top: 3px;
    font-size: 8px;
    font-weight: 700;
    letter-spacing: 1.6px;
    color: var(--brand-red);
  }
  .contact {
    position: absolute;
    left: 972px;
    top: 542px;
    font-size: 11px;
    line-height: 14px;
  }
  .contact-flag {
    display: block;
    width: 18px;
    height: 18px;
    margin-bottom: 8px;
  }
  .contact-address { margin-bottom: 11px; }
</style>
</head>
<body>
<main class="canvas">
  <h1 class="sheet-title">Folder: inside</h1>

  <section class="folder" aria-label="Folder inside spread">
    <svg class="folder-art" width="1200" height="900" viewBox="0 0 1200 900" aria-hidden="true">
      <!-- paper base -->
      <rect class="folder-paper" x="54" y="96" width="1090" height="764" fill="var(--paper)"/>
      <!-- red left panel with pocket cut -->
      <polygon class="folder-panel" fill="var(--brand-red)"
        points="54,96 948,96 948,670 632,670 610,860 54,860"/>
      <!-- right pocket fold line -->
      <polyline class="pocket-line" fill="none" stroke="var(--brand-red)" stroke-width="2"
        points="942,690 1032,836 1136,852"/>
    </svg>

    <div class="brand">
      <div class="brand-row">
        <span class="brand-name">veltrix</span>
        <span class="brand-dot"></span>
      </div>
      <span class="brand-tagline">PROMOTIONS GROUP</span>
    </div>

    <div class="contact">
      <svg class="contact-flag" viewBox="0 0 18 18" aria-hidden="true">
        <polygon points="0,0 18,0 0,18" fill="var(--brand-red)"/>
      </svg>
      <p class="contact-address">27 Calle Norte, Los Pinos,<br>Santo Domingo<br>Dominican Republic</p>
      <p class="contact-lines">Phone: +809.555.0142<br>Fax: +809.555.0148<br>E-mail: info@veltrix.com.do</p>
    </div>
  </section>
</main>
</body>
</html>
```